Larkspur Homes - wanted BRILLIANT website design for our new property investing company

We need a website design for our new company based in Bristol, England, UK called "Larkspur Homes". We help buy people property who are in financial difficulty or who are needing to sell their property quickly for reasons such as death, divorce/separation, relocation, emigration.

We have a logo being designed incorporating strawberry and property (so red and green). We would like designs to communicate an elegant ,professional, approachable, friendly
fresh clean but also warm appealing appearance
Not too busy
Website consistent with logo and company name i.e. colour scheme

Please use our word document for content as a guide but use professional judgement for minor alterations if you feel they would benefit the site/structure etc

Please ask at any time if not sure

Target Market(s)

Adult british population, those that have a mortgage / loan / own property

Industry/Entity Type

Financial

Font styles to use
Serif
Sans Serif
Decorative

Colors
0692cd
33b7a4
acd036
fbee3e
3176b5
886aae
a6479a
e567a6
eb1f27

Requirements
Must have
• This must not look like a template website we are looking for UNIQUE please!
Nice to have
• Bristol pictures instead of generic, or colourful line drawings/comic drawings of houses/property/keys/happy people.....
Should not have
• An obvious off the shelf template design

```html
<!DOCTYPE html>
<html lang="en">
<head>
<meta charset="utf-8">
<title>Larkspur Homes</title>
<link href="https://fonts.googleapis.com/css2?family=Open+Sans:wght@400;600;700&display=swap" rel="stylesheet">
<style>
:root{
  --red:#d8344a;
  --nav:#e06a78;
  --nav-dark:#c94458;
  --ink:#333;
  --muted:#777;
  --green:#5aa845;
  --green-dark:#4a9338;
  --panel:#eeeeee;
  --line:#d6d6d6;
  --footer:#2b2b2b;
}
*{box-sizing:border-box;margin:0;padding:0}
html,body{width:828px;height:1200px;overflow:hidden}
body{font-family:"Open Sans",Arial,sans-serif;color:var(--ink);background:#f4f4f4;font-size:9px}
.page{width:828px;height:1200px;background:#fff;position:relative}
.site-header{height:72px;display:flex;justify-content:space-between;align-items:center;padding:0 48px}
.brand{display:flex;align-items:center;gap:8px;font-weight:700;font-size:18px;color:var(--red);line-height:1}
.brand-mark{width:12px;height:12px;background:var(--red)}
.contact-lines{text-align:right;font-size:9px;color:var(--muted);line-height:1.6}
.contact-lines b{color:var(--red);font-weight:600}
.main-nav{height:28px;background:linear-gradient(var(--nav),var(--nav-dark));display:flex;padding-left:48px}
.main-nav a{color:#fff;text-decoration:none;font-size:9px;font-weight:600;padding:0 12px;line-height:28px;text-transform:uppercase}
.main-nav a.active{background:rgba(255,255,255,.25)}
.hero{height:312px;position:relative;background:linear-gradient(#9ed0ee 0%,#d6ecf8 55%,#7cbf4a 56%,#4f9a2c 100%)}
.hero-caption{position:absolute;left:0;right:0;top:210px;text-align:center;color:#fff;font-size:22px;text-shadow:0 1px 3px rgba(0,0,0,.5)}
.hero-dots{position:absolute;bottom:12px;left:0;right:0;display:flex;justify-content:center;gap:5px}
.hero-dots span{width:6px;height:6px;border-radius:50%;background:#fff;opacity:.6}
.hero-dots span:first-child{opacity:1}
.quick-contact{height:68px;background:linear-gradient(#f2f2f2,#e3e3e3);padding:10px 48px}
.quick-contact h3{font-size:11px;font-weight:600;color:#555;margin-bottom:6px}
.qc-row{display:flex;gap:8px}
.qc-row span{flex:1;height:18px;background:#fff;border:1px solid var(--line);font-size:7px;color:#999;padding:3px 5px}
.qc-row .btn{flex:0 0 56px;background:var(--red);color:#fff;border:none;text-align:center}
.intro{text-align:center;padding:14px 90px 0;height:82px}
.intro h2{font-size:13px;font-weight:600;margin-bottom:8px;letter-spacing:.3px}
.intro p{font-size:7.5px;color:var(--muted);line-height:1.6}
.help-box{margin:0 62px;height:208px;background:linear-gradient(var(--green),var(--green-dark));border-radius:3px;padding:12px 18px;position:relative;color:#fff}
.help-box h3{font-size:16px;font-weight:600;margin-bottom:10px}
.help-cols{display:flex;gap:14px;width:450px}
.help-cols ul{flex:1}
.tick-list{list-style:none}
.tick-list li{display:flex;align-items:center;gap:6px;font-size:8px;line-height:17px}
.tick-list li::before{content:"";width:7px;height:7px;border-radius:50%;background:currentColor;flex:none;opacity:.9}
.help-photo{position:absolute;right:18px;top:18px;width:190px;height:172px;background:linear-gradient(135deg,#f2f2f2,#cfcfcf);border-radius:3px}
.panels{display:flex;gap:10px;margin:12px 46px 0;height:168px}
.panel{flex:1;background:var(--panel);border:1px solid var(--line);padding:10px 12px;position:relative}
.panel p{font-size:8px;margin-bottom:4px;color:#444}
.panel .tick-list li{color:var(--red);line-height:15px}
.panel .tick-list li span{color:#444}
.house-photo{position:absolute;right:14px;bottom:16px;width:120px;height:96px;background:linear-gradient(#c94a3c 0%,#c94a3c 40%,#f3efe6 41%,#e4ddd0 100%);border-radius:2px}
.partners{text-align:center;padding-top:16px;height:108px}
.partners h2{font-size:13px;font-weight:600;letter-spacing:1px;margin-bottom:14px}
.partner-row{display:flex;justify-content:center;gap:30px}
.partner-row span{width:130px;height:34px;background:#e2e2e2;border-radius:3px}
.site-footer{position:absolute;left:0;right:0;bottom:0;height:145px;background:var(--footer);padding:26px 40px}
.social{display:flex;justify-content:center;gap:8px}
.social span{width:22px;height:22px;border-radius:50%;background:#5a5a5a}
.footer-base{display:flex;justify-content:space-between;align-items:center;margin-top:28px;color:#999;font-size:7.5px}
.newsletter{display:flex;gap:4px}
.newsletter span{width:110px;height:16px;background:#fff;font-size:7px;color:#999;padding:3px 5px}
.newsletter b{width:22px;height:16px;background:var(--red)}
</style>
</head>
<body>
<div class="page">
  <header class="site-header">
    <div class="brand"><span class="brand-mark"></span>Larkspur Homes</div>
    <div class="contact-lines">
      <div>PHONE: <b>0800 000 4821</b></div>
      <div>Email: <b>info@larkspur-homes.co.uk</b></div>
    </div>
  </header>
  <nav class="main-nav">
    <a class="active">Home</a><a>Sell your property fast</a><a>Rent your property fast</a><a>The 5 easy steps</a><a>About us</a><a>Contact us</a>
  </nav>
  <section class="hero" role="img" aria-label="Photo of a white house on a green hill under a blue sky">
    <div class="hero-caption">Do you want to sell or rent out your house quickly?</div>
    <div class="hero-dots"><span></span><span></span><span></span><span></span></div>
  </section>
  <section class="quick-contact">
    <h3>Quick Contact us</h3>
    <div class="qc-row"><span>Name</span><span>Email</span><span>Phone</span><span>Property address</span><span>Message</span><span class="btn">Send</span></div>
  </section>
  <section class="intro">
    <h2>WE ARE OFFERING THE BEST REAL ESTATE DEALS</h2>
    <p>Local to our region, we buy homes quickly and fairly, with no fees and no fuss. Whatever your reason for selling, we listen first and offer a simple, honest solution that works for you and your family.</p>
  </section>
  <section class="help-box">
    <h3>Who can we help?</h3>
    <div class="help-cols">
      <ul class="tick-list">
        <li>How to stop repossession</li><li>Divorce or separation</li><li>Financial problems</li><li>Don't like estate agents?</li><li>Property needing work</li><li>Retiring landlords</li><li>Negative equity</li><li>Opportunity not to be missed</li>
      </ul>
      <ul class="tick-list">
        <li>Guaranteed rent scheme</li><li>Ill health</li><li>Relocating</li><li>Inherited property</li><li>Chain collapse</li><li>Tenanted property</li>
      </ul>
    </div>
    <div class="help-photo" role="img" aria-label="Photo of hands handing over a set of house keys"></div>
  </section>
  <section class="panels">
    <div class="panel">
      <p>We are a local family run property business who also specialise in:</p>
      <ul class="tick-list">
        <li><span>Buying properties quickly</span></li><li><span>Finding creative solutions to your property problems</span></li><li><span>Property rental management</span></li><li><span>Lettings to professional and student tenants</span></li><li><span>Guaranteed rent and management schemes for landlords</span></li><li><span>Stopping repossessions</span></li><li><span>Motivated sellers</span></li><li><span>Chain fixing</span></li>
      </ul>
    </div>
    <div class="panel">
      <p>Fill in the contact form on this page OR call us on 07000 123456</p>
      <ul class="tick-list">
        <li><span>100% confidential</span></li><li><span>100% completions</span></li><li><span>Help prevent repossession or eviction</span></li><li><span>Help solve any property problems</span></li><li><span>No estate agent fees</span></li><li><span>Any debt paid by us</span></li><li><span>Quick purchases, quick turnaround</span></li><li><span>Once agreed we guarantee a sale</span></li>
      </ul>
      <div class="house-photo" role="img" aria-label="Picture of a small house model with a red roof"></div>
    </div>
  </section>
  <section class="partners">
    <h2>PARTNERS</h2>
    <div class="partner-row"><span></span><span></span><span></span><span></span></div>
  </section>
  <footer class="site-footer">
    <div class="social"><span></span><span></span><span></span><span></span><span></span><span></span></div>
    <div class="footer-base">
      <div>Copyright © Larkspur Homes. All rights reserved.</div>
      <div class="newsletter"><span>Email address</span><b></b></div>
    </div>
  </footer>
</div>
</body>
</html>
```